Unique Mendrix Building Bussiness Card Design

www.mendrix.com.au

Please see website for Company profile. We require a design that incorporates our logo colours and is unique in shape and style compared to all other business cards.

www.mendrix.com.au

INSPIRE US !!!
Updates

Target Market(s)

Facility managers, Building Managers, Architects

Industry/Entity Type

Business

Contact Information for Business Card

Mendrix Building Solutions
Project Manager
Dennis Harwood
0437 619 204
Sales@mendrix.com.au

Logo Text

Mendrix Building Solutions

Logo styles of interest
Abstract Logo
Requirements
Nice to have
• Card must show we are an established big business to trust.

```html
<!DOCTYPE html>
<html lang="en">
<head>
<meta charset="utf-8">
<title>Mendrix Business Card</title>
<link rel="stylesheet" href="https://fonts.googleapis.com/css2?family=Open+Sans:wght@400;600;700&display=swap">
<style>
  :root {
    --stage: #5b5b5b;
    --card-white: #ffffff;
    --red-deep: #b8232b;
    --red: #c7302a;
    --orange-glow: #e8691f;
    --brand-red: #a9232a;
    --accent-orange: #e0601f;
    --rule: #d9d9d9;
    --ink-white: #ffffff;
  }
  * { margin: 0; padding: 0; box-sizing: border-box; }
  html, body {
    width: 1200px; height: 1044px; overflow: hidden;
    background: var(--stage);
    font-family: "Open Sans", Arial, sans-serif;
  }
  .stage {
    position: relative; width: 1200px; height: 1044px;
    display: flex; align-items: center; justify-content: center; gap: 40px;
  }
  .card {
    position: relative; width: 540px; height: 302px;
    box-shadow: 0 6px 18px rgba(0,0,0,.35);
  }
  .card--front {
    background: radial-gradient(ellipse 60% 65% at 48% 42%, var(--orange-glow) 0%, var(--red) 60%, var(--red-deep) 100%);
    color: var(--ink-white);
  }
  .card--back { background: var(--card-white); }
  .brand {
    position: absolute; display: flex; align-items: center; gap: 10px;
    font-weight: 700; letter-spacing: .5px;
  }
  .brand-square { width: 22px; height: 22px; }
  .card--front .brand { left: 50%; top: 128px; transform: translateX(-50%); font-size: 38px; color: var(--ink-white); }
  .card--front .brand-square { background: var(--ink-white); }
  .website {
    position: absolute; left: 0; right: 0; bottom: 24px;
    text-align: center; font-size: 13px; color: var(--ink-white);
  }
  .card--back .brand { left: 50%; top: 62px; transform: translateX(-50%); font-size: 34px; color: var(--brand-red); }
  .card--back .brand-square { background: var(--accent-orange); }
  .person { position: absolute; left: 0; right: 0; top: 156px; text-align: center; line-height: 1.35; }
  .person-name { font-size: 14px; color: var(--brand-red); }
  .person-title { font-size: 14px; color: var(--accent-orange); }
  .divider { position: absolute; left: 20px; right: 20px; top: 242px; height: 1px; background: var(--rule); }
  .contacts {
    position: absolute; left: 0; right: 0; top: 256px;
    display: flex; justify-content: center; gap: 26px;
    font-size: 13px; color: var(--accent-orange);
  }
  .contact { display: flex; align-items: center; gap: 6px; }
  .contact svg { width: 13px; height: 13px; }
</style>
</head>
<body>
<main class="stage">
  <section class="card card--front" aria-label="Card front">
    <div class="brand"><span class="brand-square"></span>Mendrix</div>
    <p class="website">www.mendrix.com.au</p>
  </section>

  <section class="card card--back" aria-label="Card back">
    <div class="brand"><span class="brand-square"></span>Mendrix</div>
    <div class="person">
      <p class="person-name">Dennis Harwood</p>
      <p class="person-title">Project Manager</p>
    </div>
    <div class="divider"></div>
    <div class="contacts">
      <span class="contact">
        <svg viewBox="0 0 16 16" aria-hidden="true"><circle cx="8" cy="8" r="6.5" fill="none" stroke="#c7302a" stroke-width="1.4"/><path d="M6 4.5 L7.5 7 L6.8 8 Q7.5 9.5 9 10.2 L10 9.5 L11.5 11 Q10.5 12.5 9 12 Q5 10.5 4.5 6.5 Q4.5 5 6 4.5Z" fill="#c7302a"/></svg>
        0437 619 204
      </span>
      <span class="contact">
        <svg viewBox="0 0 16 16" aria-hidden="true"><rect x="1.5" y="3.5" width="13" height="9" fill="none" stroke="#c7302a" stroke-width="1.3"/><path d="M1.5 3.5 L8 9 L14.5 3.5" fill="none" stroke="#c7302a" stroke-width="1.3"/></svg>
        Sales@mendrix.com.au
      </span>
    </div>
  </section>
</main>
</body>
</html>
```